Mirela Causo Photography

I need a website design for my photography business, I want something clean, elegant, Classy.. I like the colors, White, Black, Green/Blue, Pink, Brown, Lavender,, I have a lot added my Logo .... Additional Info... I need a Photography Website Design, with probably 6 Tabs, Home, About Me, Portfolio, Gallery, Investment, Contact.
Home Page should have my logo, Name & Address, Social Media Icons, and Pictures.
As long as the templates are made I have a hosting coming that will code it.
Target Market(s)
Portraits Photography, Senior Portraits, Newborn, Families, Events, Engagements, Wedding,
Industry/Entity Type
Business
Number of Pages Required
5+ page
Look and feel

```html
<!DOCTYPE html>
<html lang="en">
<head>
<meta charset="utf-8">
<title>Mirela Causo Photography</title>
<link rel="stylesheet" href="https://fonts.googleapis.com/css2?family=Oswald:wght@300;400&display=swap">
<style>
  :root {
    --teal: #10a58f;
    --teal-dark: #0d8f7c;
    --hero-bg: #eef0f1;
    --ink: #4a4a4a;
    --nav-ink: #555555;
    --footer-bg: #2b2b2b;
    --footer-text: #b8b8b8;
    --footer-muted: #9a9a9a;
    --pink: #f29bbd;
    --icon-grey: #c4c4c4;
    --white: #ffffff;
  }
  * { margin: 0; padding: 0; box-sizing: border-box; }
  html, body { width: 1200px; height: 1000px; overflow: hidden; }
  body { position: relative; font-family: Arial, Helvetica, sans-serif; background: var(--footer-bg); }

  .hero {
    position: absolute; left: 0; top: 0; width: 1200px; height: 630px;
    background: radial-gradient(ellipse at 35% 40%, #dfe2e4 0%, #e9ebec 40%, var(--hero-bg) 75%);
    overflow: hidden;
  }
  .brand { position: absolute; left: 195px; top: 24px; display: flex; align-items: center; gap: 12px; }
  .brand-dot { width: 42px; height: 42px; border-radius: 50%; background: #3a3a3a; }
  .brand-name {
    font-family: 'Oswald', sans-serif; font-weight: 300; color: #3a3a3a;
    font-size: 26px; line-height: 30px; letter-spacing: 1px;
  }
  .brand-name span { display: block; font-size: 13px; line-height: 18px; letter-spacing: 5px; }

  .main-nav { position: absolute; top: 52px; left: 520px; font-family: 'Oswald', sans-serif; font-size: 12px; letter-spacing: .3px; }
  .main-nav a { position: absolute; white-space: nowrap; color: var(--nav-ink); text-decoration: none; }
  .main-nav a.is-active { color: var(--teal); }
  .main-nav a.is-active::after { content: ""; position: absolute; left: 0; right: 0; top: 23px; height: 2px; background: var(--teal); }
  .social-top { position: absolute; top: 52px; left: 942px; display: flex; gap: 9px; }
  .social-top span { width: 18px; height: 18px; border-radius: 50%; background: var(--icon-grey); }

  .mosaic { position: absolute; left: 0; top: 0; }

  .feature {
    position: absolute; left: 497px; top: 455px; width: 160px; text-align: center; color: var(--white);
  }
  .feature-title { font-family: 'Oswald', sans-serif; font-weight: 400; font-size: 13px; letter-spacing: .3px; }
  .feature-rule { width: 68px; height: 1px; background: rgba(255,255,255,.8); margin: 6px auto 8px; }
  .feature-text { font-size: 8.5px; line-height: 12px; color: #083d36; }
  .feature-more { display: inline-block; margin-top: 14px; font-size: 8.5px; color: var(--white); text-decoration: underline; }

  .footer-col { position: absolute; top: 696px; }
  .footer-heading { font-family: 'Oswald', sans-serif; font-weight: 400; font-size: 20px; color: var(--teal); margin-bottom: 22px; }
  .welcome { left: 194px; width: 360px; }
  .welcome p { font-size: 11px; line-height: 16.5px; color: var(--footer-text); margin-bottom: 15px; }
  .contacts { left: 611px; width: 190px; }
  .contacts .intro { font-size: 8.5px; line-height: 12px; color: var(--footer-text); padding-left: 3px; }
  .contacts .call-label { font-size: 9.5px; font-weight: bold; color: var(--footer-muted); margin-top: 14px; padding-left: 3px; }
  .contacts .phone { font-size: 18px; color: var(--pink); letter-spacing: .5px; padding-left: 3px; }
  .contacts .email { font-size: 8.5px; color: var(--footer-text); margin-top: 6px; padding-left: 3px; }
  .skills { left: 837px; width: 200px; }
  .skills ul { list-style: none; }
  .skills li { position: relative; padding-left: 18px; font-size: 10.5px; color: var(--footer-text); line-height: 24.5px; }
  .skills li::before { content: ""; position: absolute; left: 2px; top: 10px; width: 5px; height: 5px; border-radius: 50%; background: var(--teal); }

  .footer-line { position: absolute; left: 0; top: 944px; width: 1200px; height: 1px; background: var(--teal-dark); }
  .footer-social {
    position: absolute; left: 542px; top: 927px; width: 124px; height: 34px; border-radius: 17px;
    background: var(--teal); display: flex; justify-content: center; align-items: center; gap: 13px;
  }
  .footer-social span { width: 20px; height: 20px; border-radius: 50%; background: #1f2a28; }
  .copyright { position: absolute; left: 0; width: 1200px; top: 972px; text-align: center; font-size: 9.5px; color: #8a8a8a; }
</style>
</head>
<body>
  <header class="hero">
    <div role="img" aria-label="Blurred street photograph backdrop" style="position:absolute;inset:0;background:linear-gradient(90deg,rgba(200,204,206,.35),rgba(240,241,242,0) 40%,rgba(215,218,220,.25));"></div>

    <svg class="mosaic" width="1200" height="630" viewBox="0 0 1200 630">
      <defs>
        <linearGradient id="g-back" x1="0" y1="0" x2="1" y2="1"><stop offset="0" stop-color="#c9a27a"/><stop offset="1" stop-color="#2f3650"/></linearGradient>
        <linearGradient id="g-bride" x1="0" y1="0" x2="1" y2="1"><stop offset="0" stop-color="#b9a34a"/><stop offset="1" stop-color="#e8e2dc"/></linearGradient>
        <linearGradient id="g-rider" x1="0" y1="0" x2="1" y2="1"><stop offset="0" stop-color="#f0e6b8"/><stop offset="1" stop-color="#a86a2a"/></linearGradient>
        <linearGradient id="g-bike" x1="0" y1="0" x2="1" y2="1"><stop offset="0" stop-color="#c7cfcf"/><stop offset="1" stop-color="#3c3a34"/></linearGradient>
        <linearGradient id="g-house" x1="0" y1="0" x2="1" y2="1"><stop offset="0" stop-color="#e0e6ea"/><stop offset=".4" stop-color="#d4483a"/><stop offset="1" stop-color="#8e2a22"/></linearGradient>
        <linearGradient id="g-portrait" x1="0" y1="0" x2="1" y2="1"><stop offset="0" stop-color="#e0b59a"/><stop offset="1" stop-color="#2a2628"/></linearGradient>
        <linearGradient id="g-horse" x1="0" y1="0" x2="1" y2="1"><stop offset="0" stop-color="#f2f2f0"/><stop offset=".6" stop-color="#5a5a58"/><stop offset="1" stop-color="#d8d8d6"/></linearGradient>
      </defs>
      <g role="img" aria-label="Photo of a woman in a hoodie seen from behind"><polygon points="455,60 565,170 455,280 345,170" fill="url(#g-back)"/></g>
      <g role="img" aria-label="Bridal portrait with lace dress and earrings"><polygon points="625,107 735,217 625,327 515,217" fill="url(#g-bride)"/></g>
      <g role="img" aria-label="Rancher herding cattle at sunset"><polygon points="790,159 900,269 790,379 680,269" fill="url(#g-rider)"/></g>
      <g role="img" aria-label="BMX bike by a railing"><polygon points="356,287 465,395 356,503 246,395" fill="url(#g-bike)"/></g>
      <g role="img" aria-label="Red townhouse facade"><polygon points="518,220 628,330 518,440 408,330" fill="url(#g-house)"/></g>
      <g role="img" aria-label="Portrait of a woman in a fur collar"><polygon points="680,275 790,385 680,495 570,385" fill="url(#g-portrait)"/></g>
      <g role="img" aria-label="Black and white photo of a running horse"><polygon points="851,323 961,433 851,543 741,433" fill="url(#g-horse)"/></g>
      <polygon points="577,385 687,495 577,605 466,495" fill="var(--teal)"/>
      <path d="M573 548 v9 l2.5 -2 l2 4 l1.6 -.8 l-2 -4 l3.2 0 z" fill="#fff" stroke="#333" stroke-width=".6"/>
    </svg>

    <div class="brand">
      <div class="brand-dot"></div>
      <div class="brand-name">Mirela Causo<span>PHOTOGRAPHY</span></div>
    </div>

    <nav class="main-nav">
      <a class="is-active" style="left:0">HOME</a>
      <a style="left:55px">ABOUT ME</a>
      <a style="left:124px">PORTFOLIO</a>
      <a style="left:200px">GALLERY</a>
      <a style="left:269px">INVESTMENT</a>
      <a style="left:358px">CONTACT</a>
    </nav>
    <div class="social-top"><span></span><span></span><span></span></div>

    <div class="feature">
      <div class="feature-title">LOREM IPSUM DUMMY</div>
      <div class="feature-rule"></div>
      <p class="feature-text">Lorem ipsum dolor sit amet, consectetur adipiscing elit, sed do eiusmod tempor incididunt</p>
      <a class="feature-more">MORE</a>
    </div>
  </header>

  <section class="footer-col welcome">
    <h2 class="footer-heading">Welcome Message</h2>
    <p>Lorem ipsum dolor sit amet, consectetur adipiscing elit, sed do eiusmod tempor incididunt ut labore et dolore magna aliqua. Ut enim ad minim veniam, quis nostrud exercitation ullamco laboris nisi ut aliquip ex ea commodo consequat.</p>
    <p>Duis aute irure dolor in reprehenderit in voluptate velit esse cillum dolore eu fugiat nulla pariatur. Excepteur sint occaecat cupidatat non proident, sunt in culpa qui officia deserunt mollit anim id est laborum.</p>
  </section>

  <section class="footer-col contacts">
    <h2 class="footer-heading">Contacts</h2>
    <p class="intro">Lorem ipsum dolor sit amet, consectetur adipisc-ing elit, sed do eiusmod tempor incididunt ut labore et dolore magna aliqua.</p>
    <p class="call-label">CALL :</p>
    <p class="phone">123 4567 8900</p>
    <p class="email">Email: info@example.com</p>
  </section>

  <section class="footer-col skills">
    <h2 class="footer-heading">Skills</h2>
    <ul>
      <li>Lorem ipsum dolor sit amet</li>
      <li>Duis aute irure dolor</li>
      <li>Reprehenderit in voluptate</li>
      <li>Velit esse cillum dolore eu fugiat</li>
      <li>Nulla pariatur</li>
      <li>Excepteur sint occaecat cupidatat</li>
    </ul>
  </section>

  <div class="footer-line"></div>
  <div class="footer-social"><span></span><span></span><span></span></div>
  <p class="copyright">Copyright © 2015 Mirela Causo Photography</p>
</body>
</html>
```